Site Re-Design For IT/Internet Services Site

Hi, We need a redevopment of our existing website (www.pelvaru.com)
Pages That need designing are:
- Content Page (existing page: http://www.pelvaru.com)
- Hotspot Locations Page (existing page: Http://www.pelvaru.com/hotspot-locations/hotspot-locations.asp)
- Form page layout, including textbox, checkbox, radio buttons, drop down, submit/reset buttons, "required fields error message"
- Design of our subscription "plan selection" content page (https://secure.pelvaru.com/?location=1001)
- Design of the NEXT TWO pages in the above subscription form, the "email/password page, to see this select less than 3 months, 1 hour, then continue and also the credit card page, see this by filling out left hand side "new account" form and continue Specs:
- The same navigation will be retained, but should be easily modifyable via PSD file.

- NOTE THAT FOR THE DESIGN COMPETITION, ONLY the CONTENT PAGE needs to be designed

- Existing Logo to Be Maintained and COMPLETELY UNCHANGE IN ANY ASPECT
- Similar format of dual navigation required. Currently main nav is horizontal with sub nav below, and "extra" nav available on left vertical strip. Does have to stay in this format, however main nav with subnav, and "extra" nav spots must be available
- Design should be fresh and innovative
- Colors are negotiable however typical design nono's will not be accepted (black content area etc) Code Requirements:
- PSD file should contain overall design, as well as sub PSD files for navigation to be easily re-created at a later date where required.

By negotiation after sucessful design chosen, extra design aspects such as: psd cutup in html, HTML markup compatible with IE6+, Chrome, Firefox required - Seperate CSS stylesheet - Images in sub folders as appropriate may be required.

Internet

5+ pages

• black background, etc.

```html
<!DOCTYPE html>
<html lang="en">
<head>
<meta charset="utf-8">
<title>Pelvaru – Contact</title>
<link href="https://fonts.googleapis.com/css2?family=Arimo:wght@400;700&family=Questrial&display=swap" rel="stylesheet">
<style>
:root{
  --blue-dark:#0f5ea3;
  --blue-mid:#1f7cc4;
  --blue-light:#4fa3e0;
  --blue-title:#0a62a8;
  --green:#a9c623;
  --green-light:#c8df48;
  --green-dark:#7f9a12;
  --grey-panel:#e6e5e6;
  --grey-line:#b9b9b9;
  --text:#3a3a3a;
  --red:#cc1010;
  --white:#ffffff;
}
*{box-sizing:border-box;margin:0;padding:0}
html,body{width:1200px;height:922px;overflow:hidden;background:var(--white);font-family:"Arimo",Arial,sans-serif;color:var(--text)}
.page{position:relative;width:1200px;height:922px;overflow:hidden}
.abs{position:absolute}

/* header */
.header-band{left:0;top:0;width:1200px;height:170px;background:linear-gradient(180deg,#2b8ad6 0%,#1b72bd 55%,#0f5aa0 100%)}
.logo-box{left:233px;top:15px;width:148px;height:139px;background:var(--white);border:4px solid var(--green);border-radius:3px;display:flex;align-items:center;justify-content:center;gap:6px}
.logo-box .mark{width:12px;height:12px;background:var(--blue-dark)}
.logo-box .name{font-family:"Arimo",Arial,sans-serif;font-weight:700;font-size:17px;color:var(--blue-dark);letter-spacing:1px}
.badge{width:65px;height:65px;background:var(--white);border:4px solid var(--green);border-radius:3px;display:flex;align-items:center;justify-content:center}
.badge span{display:block;width:34px;height:34px;border-radius:50%;background:linear-gradient(180deg,#d8d8d8,#9c9c9c)}
.badge.square span{border-radius:6px;width:38px;height:26px}
.search-panel{left:463px;top:16px;width:495px;height:138px;border-radius:6px;background:linear-gradient(135deg,#5aaeea 0%,#3c94d9 45%,#2a7fc8 100%)}
.brand-box{left:650px;top:30px;width:63px;height:24px;background:var(--white);border-radius:5px;border:1px solid #9bc2e2;font-size:12px;color:#3a6ea5;display:flex;align-items:center;justify-content:center}
.search-input{left:718px;top:34px;width:168px;height:17px;background:var(--white);border:1px solid #8fb2cf}
.search-btn{left:891px;top:34px;width:47px;height:17px;border-radius:8px;background:linear-gradient(180deg,#d6ea59,#a4c21f);font-size:8px;color:#2d4a0a;display:flex;align-items:center;justify-content:center}
.radio-row{top:58px;font-size:8px;color:var(--white);display:flex;align-items:center;gap:4px}
.radio-row i{display:inline-block;width:8px;height:8px;border-radius:50%;background:var(--white);border:1px solid #7aa}
.util-bar{left:538px;top:122px;width:416px;height:28px;background:linear-gradient(180deg,#3b8fd4,#2a79bf);display:flex;align-items:center}
.util-item{flex:1;display:flex;align-items:center;justify-content:center;gap:6px;font-size:10.5px;color:#dbeeff;border-right:1px solid #5ea4de;height:20px}
.util-item:last-child{border-right:none}
.util-item svg{width:13px;height:13px}

/* main nav */
.nav{left:0;top:170px;width:1200px;height:33px;background:linear-gradient(180deg,#c7dd45 0%,#a9c623 30%,#9ab91b 100%);border-bottom:3px solid #d8ea6c}
.nav-list{position:absolute;left:233px;top:2px;height:28px;display:flex;list-style:none;border-left:1px solid #8fa817}
.nav-list li{font-size:11.5px;color:#1e2a05;display:flex;align-items:center;justify-content:center;border-right:1px solid #8fa817;position:relative}
.nav-list li.active{background:linear-gradient(180deg,#d2e65a,#b6cf31)}
.nav-list li.active::after{content:"";position:absolute;bottom:0;left:50%;margin-left:-4px;border:4px solid transparent;border-bottom-color:#7f9a12}
.subnav{left:501px;top:202px;width:150px;height:84px;background:var(--green);padding:4px 4px;list-style:none;z-index:5}
.subnav li{height:20px;display:flex;align-items:center;gap:5px;padding-left:5px;font-size:10px;color:var(--white);border-bottom:1px solid #c7dc52}
.subnav li:last-child{border-bottom:none}
.subnav li::before{content:"";border:3px solid transparent;border-left:4px solid #3d4d06}
.subnav li.current{background:#bcd43e}

/* content */
.crumb{left:235px;top:216px;font-size:9px;font-weight:700;color:#555}
.promo{left:233px;top:241px;width:174px;height:81px;border:2px solid #c9c9c9;border-radius:3px;background:linear-gradient(180deg,#fbfbfb,#e4e4e4);overflow:hidden}
.promo-art{position:absolute;left:0;top:0;width:72px;height:77px;background:radial-gradient(circle at 35% 45%,#c6e1f3 0%,#9cc7e6 45%,#e4e4e4 85%)}
.promo-text{position:absolute;left:75px;top:4px;font-family:"Questrial",Arial,sans-serif;line-height:1}
.promo-text .l1{font-size:20px;color:#3b88c8}
.promo-text .l1 b{font-weight:400;color:#3b88c8}
.promo-text .l2{font-size:16px;color:#9aa6b3;margin-top:2px}
.promo-text .l2 b{font-weight:700;color:#6aaee0}
.promo-text .l3{font-size:24px;color:#7a7a7a;margin-top:0}
.promo-text .l3 b{font-weight:700;color:#3b88c8}
.title{left:423px;top:228px;font-family:"Questrial",Arial,sans-serif;font-size:25px;color:var(--blue-title)}
.intro{left:424px;top:270px;width:532px;font-size:9.6px;line-height:16.5px;color:#333;text-align:justify}

.form-panel{left:424px;top:333px;width:532px;height:448px;background:var(--grey-panel)}
.label{font-size:10.5px;font-weight:700;color:#333}
.label em{font-style:normal;color:var(--red)}
.field{height:18px;background:var(--white);border:1px solid #a8a8a8;font-size:9.5px;padding:2px 5px;color:#333}
.opt{font-size:9.5px;color:#333;display:flex;align-items:center;gap:7px}
.opt .r{width:9px;height:9px;border-radius:50%;border:1px solid #555;background:var(--white)}
.opt .c{width:9px;height:9px;border:1px solid #4a7fae;background:var(--white);position:relative}
.select{left:699px;top:415px;width:202px;height:18px;background:var(--white);border:1px solid #a8a8a8;font-size:9.5px;padding:2px 5px}
.select-arrow{position:absolute;right:2px;top:2px;width:12px;height:12px;background:linear-gradient(180deg,#e9f1fb,#b9d1ee);border:1px solid #7f9db9}
.list{left:699px;top:433px;width:202px;height:119px;background:var(--white);border:1px solid #7f9db9;font-size:9.3px;overflow:hidden}
.list div{height:11.7px;line-height:11.7px;padding-left:3px}
.list .sel{background:#316ac5;color:var(--white);margin-right:14px}
.scroll{position:absolute;right:0;top:0;width:13px;height:100%;background:#eef2f8;border-left:1px solid #d5dde8}
.textarea{left:477px;top:607px;width:424px;height:78px;background:var(--white);border:1px solid #a8a8a8}
.error{left:478px;top:696px;width:424px;height:28px;background:var(--white);border:1px solid var(--green);font-size:9.8px;font-weight:700;color:var(--red);padding:8px 8px}
.btn{top:741px;height:19px;border-radius:9px;background:linear-gradient(180deg,#dcdcdc,#a2a2a2);border:1px solid #8a8a8a;font-size:10px;font-weight:700;color:#333;display:flex;align-items:center;justify-content:center;gap:3px}

/* footer */
.footer{left:233px;top:810px;width:723px;height:85px;border:2px solid #7f9a12;border-radius:5px;background:linear-gradient(180deg,#b3cc2c 0%,#9ab71c 100%)}
.footer-site{left:253px;top:820px;font-size:29px;font-weight:700;color:#1d6db7;letter-spacing:-0.5px}
.footer-rule{left:253px;top:859px;width:233px;height:1px;background:#d4e67a}
.footer-phone{left:256px;top:867px;font-size:13.5px;color:#d9e6a3}
.footer-div{left:507px;top:816px;width:1px;height:74px;background:#6e8710}
.flink{font-size:9px;color:#f3f8da;display:flex;align-items:center;gap:5px}
.flink::before{content:"";width:8px;height:1px;background:#2c6fb5;box-shadow:0 0 0 0 transparent;border-right:3px solid #2c6fb5}
.copy{right:246px;top:903px;font-size:8px;color:#3a7bc0}
</style>
</head>
<body>
<div class="page">

  <!-- header -->
  <div class="abs header-band"></div>
  <div class="abs logo-box"><span class="mark"></span><span class="name">PELVARU</span></div>
  <div class="abs badge" style="left:389px;top:16px"><span></span></div>
  <div class="abs badge" style="left:389px;top:89px"><span></span></div>
  <div class="abs badge square" style="left:462px;top:89px"><span></span></div>

  <div class="abs search-panel"></div>
  <div class="abs brand-box">Seekora</div>
  <div class="abs search-input"></div>
  <div class="abs search-btn">SEARCH</div>
  <div class="abs radio-row" style="left:721px"><i></i>Web</div>
  <div class="abs radio-row" style="left:768px"><i></i>www.pelvaru.com</div>
  <div class="abs radio-row" style="left:857px"><i></i>secure.pelvaru.com</div>

  <div class="abs util-bar">
    <div class="util-item">
      <svg viewBox="0 0 14 14"><circle cx="7" cy="7" r="6.5" fill="#6ab4f0" stroke="#fff" stroke-width="1"/><rect x="6" y="6" width="2" height="5" fill="#fff"/><circle cx="7" cy="4" r="1.1" fill="#fff"/></svg>FAQ'S</div>
    <div class="util-item">
      <svg viewBox="0 0 14 14"><circle cx="7" cy="7" r="6" fill="none" stroke="#9fd0f5" stroke-width="1.6"/><circle cx="7" cy="7" r="2.4" fill="none" stroke="#9fd0f5" stroke-width="1.4"/></svg>CONTACT US</div>
    <div class="util-item">
      <svg viewBox="0 0 14 14"><circle cx="7" cy="4" r="3" fill="#8cc6f2"/><path d="M1.5 13c0-4 2.5-5.5 5.5-5.5s5.5 1.5 5.5 5.5z" fill="#8cc6f2"/></svg>MY ACCOUNT</div>
  </div>

  <!-- main navigation -->
  <div class="abs nav">
    <ul class="nav-list">
      <li style="width:95px">HOME</li>
      <li style="width:172px">WIRELESS HOTSPOTS</li>
      <li class="active" style="width:150px">INTERNET KIOSKS</li>
      <li style="width:182px">HOTSPOT LOCATIONS</li>
      <li style="width:123px">RESELLERS</li>
    </ul>
  </div>

  <!-- content -->
  <div class="abs crumb">Home</div>
  <div class="abs promo">
    <div class="promo-art" role="img" aria-label="Wireless signal illustration"></div>
    <div class="promo-text">
      <div class="l1"><b>We</b> have</div>
      <div class="l2">the <b>solution</b></div>
      <div class="l3">for <b>you</b></div>
    </div>
  </div>

  <div class="abs title">Contact</div>
  <p class="abs intro">Although a staggering number of people around the world are now online, many are still tethered to their desks when accessing the internet. Pelvaru's vision is to create a world of ubiquitous wireless internet access, without sacrificing the rich experience you get from your office, school, or home. In today's fast-moving world, people are used to being able to access the services</p>

  <ul class="abs subnav">
    <li>Feautres</li>
    <li class="current">Benefits</li>
    <li>Kioks types</li>
    <li>Prices</li>
  </ul>

  <div class="abs form-panel"></div>
  <div class="abs label" style="left:478px;top:348px">Name <em>*</em></div>
  <div class="abs field" style="left:478px;top:364px;width:203px">Dayana</div>
  <div class="abs label" style="left:699px;top:349px">Last Name <em>*</em></div>
  <div class="abs field" style="left:699px;top:364px;width:202px"></div>

  <div class="abs label" style="left:478px;top:399px">Age</div>
  <div class="abs field" style="left:478px;top:415px;width:203px"></div>
  <div class="abs label" style="left:699px;top:400px">Country</div>
  <div class="abs select">- Select -
    <span class="select-arrow"><svg viewBox="0 0 12 12" width="10" height="10"><path d="M3 4.5l3 3 3-3" fill="none" stroke="#3b5f8c" stroke-width="1.6"/></svg></span>
  </div>
  <div class="abs list">
    <div class="sel">- Select -</div>
    <div>Afganistan</div>
    <div>Albania</div>
    <div>Algeria</div>
    <div>American Samoa</div>
    <div>Azerbaijan</div>
    <div>Bahamas</div>
    <div>Bahrain</div>
    <div>Bangladsh</div>
    <div>Barbados</div>
    <span class="scroll"></span>
  </div>

  <div class="abs label" style="left:478px;top:449px">Subject</div>
  <div class="abs opt" style="left:478px;top:470px"><span class="r"></span>Service</div>
  <div class="abs opt" style="left:478px;top:491px"><span class="r"></span>Info</div>

  <div class="abs label" style="left:478px;top:517px">What do you think about our service?</div>
  <div class="abs opt" style="left:478px;top:537px"><span class="c"></span>Excellent</div>
  <div class="abs opt" style="left:478px;top:557px"><span class="c"><svg viewBox="0 0 9 9" width="7" height="7" style="position:absolute;left:0;top:0"><path d="M1.5 4.5l2 2 4-5" fill="none" stroke="#2a8a1a" stroke-width="1.6"/></svg></span>Good</div>

  <div class="abs label" style="left:477px;top:587px">Enter your Comments or questions below <em>*</em></div>
  <div class="abs textarea"></div>
  <div class="abs error">Please fill up the required fields. “Name” “Last Name” “Comments”</div>

  <div class="abs btn" style="left:477px;width:54px">CLEAR</div>
  <div class="abs btn" style="left:540px;width:56px">SEND<svg viewBox="0 0 12 10" width="10" height="8"><path d="M1 1l4 4-4 4M6 1l4 4-4 4" fill="none" stroke="#1d6db7" stroke-width="2"/></svg></div>

  <!-- footer -->
  <div class="abs footer"></div>
  <div class="abs footer-site">www.pelvaru.com</div>
  <div class="abs footer-rule"></div>
  <div class="abs footer-phone">T: 1800 472 615 &nbsp; F: (07) 3184 2290</div>
  <div class="abs footer-div"></div>

  <div class="abs flink" style="left:525px;top:824px">HOME</div>
  <div class="abs flink" style="left:525px;top:847px">WIRELESS HOTSPOTS</div>
  <div class="abs flink" style="left:525px;top:870px">INTERNET KIOSKS</div>
  <div class="abs flink" style="left:665px;top:824px">HOTSPOT LOCATIONS</div>
  <div class="abs flink" style="left:665px;top:847px">RESELLERS</div>
  <div class="abs flink" style="left:665px;top:870px">FAQ'S</div>
  <div class="abs flink" style="left:814px;top:824px">CONTACT US</div>
  <div class="abs flink" style="left:814px;top:847px">MY ACCOUNT</div>

  <div class="abs copy">All Content Copyright Pelvaru Pty Ltd 2006</div>
</div>
</body>
</html>
```